Vorlen - Customer Experience Software Company Web Design

*****UPDATE*****
We've been getting a lot of corporate designs through. Unfortunately this is not what we are looking for. We would like our brand to be more approachable and for the look and feel to to be a bit more fun.
Also the best designs we have received so far have followed the "less is more" approach. Im hoping any news designs will take these aspects into account.
*****************

Background:

Vorlen is a Customer Experience Technology company. We equip business and technology teams with the frameworks, tools and services to help them create compelling experiences for their customers.

Our flagship product - Vorlen CX is an open-source customer experience application framework – it enables organisation to build highly differentiated business applications to deliver compelling experiences to your customers.

Vorlen CX is designed for innovators who understand that unlocking opportunity in today’s competitive marketplace is driven by delivering a better customer experience.

Task:

We are looking for a web design (we need PSD, no HTML/CSS) for our company site through which to launch our customer experience framework product. The site will be also used as a support site, so the functional aspect of the site is as important as the visual impact for sales.

In order to help us conceptualise ideas and content we have drafted a temporary website using a standard wordpress theme (please see details below). Now we have a general idea of our requirements we like we would like to take it to the next level and get some designs with that professional edge.

Our target market are Enterprise organisations - that is senior members of the business & technology teams (Business General Managers, CTO’s, CIO’s, and Senior Architects and Senior Developers). We want something clean & fresh which is DIFFERENT from the typical corporate technology websites out there. We would like to be seen as more approachable than most large technology companies.

Words we would like to use to describe the finished design:
• Clean (we’re thinking white background with one or two key colours)
• Fresh
• Light
• Modern
• Less is more
• Web 2.0
• Fun but professional (aimed at Enterprise/Large organisations)
• Bold, clear call to action – e.g. Live Demo & Download
• Readable (but Sans Serif)

As we’re a Customer Experience company, the usability of the site is critical. The site must be functional, intuitive & easy to navigate. We want to keep the number of user clicks to the bare minimum possible.

Other aspects, which we would like to incorporate into the site
• Home Page banner slider
• Client logon
• Newsletter sign up
• Social media links – Friendwall, Linkfolio (for starters)
• Rich footer links

Some websites we like
• http://brightpanelworks.example - clean, light, modern & intuitive
• http://www.tamsoledrik.example - bold, clear messaging
• http://www.opengridhub.example/markup/emblem - punchy, colourful
• http://postwren.example/ - modern, clear messaging, colourful, rich footer area

Target Market(s)

Enterprise organisations - that is senior members of the business & technology teams (Business General Managers, CTO’s, CIO’s, Senior Devs)

Industry/Entity Type

Business

Requirements
Must have
• - Design Specs: Accepted file formats: During the design phase adobe PSD or JPEG are OK (if you need to upload files), but for the handover we'll need PSD only with all the original layers.
- The width needs to be a size that will work with every size computer screen
- Need to use cross-platform compatible font
- The graphic elements used for the design must be copyright free

Current test site
- URL http://vorlen.example/wp-admin
- username: artmarket
- password: artmarket

IMPORTANT NOTE REGARDING OUR CURRENT TEST SITE:

This is a very basic version of a site to help us generate requirements. This design is only a starting point/input and is not locked in stone i.e. we do not simply want this site simply tweaked around the edges.

We are looking for you to use all of your graphic design skills and experience to create a truly awesome site design!

```html
<!DOCTYPE html>
<html lang="en">
<head>
<meta charset="utf-8">
<title>Vorlen – The Customer Experience Framework</title>
<link rel="stylesheet" href="https://fonts.googleapis.com/css2?family=Source+Sans+3:ital,wght@0,400;0,600;0,700;1,400&display=swap">
<style>
  :root {
    --pink: #e0336a;
    --pink-dark: #c81f55;
    --pink-soft: #f3a9c1;
    --ink: #333333;
    --text: #5a5a5a;
    --muted: #7d7d7d;
    --rule: #555555;
    --paper: #ffffff;
    --footer: #1c1c1c;
    --footer-deep: #141414;
    --footer-text: #d6d6d6;
  }
  * { margin: 0; padding: 0; box-sizing: border-box; }
  html, body { width: 1200px; height: 1162px; overflow: hidden; }
  body {
    position: relative;
    font-family: "Source Sans 3", sans-serif;
    color: var(--text);
    background: linear-gradient(180deg, #f1f1f1 0, var(--paper) 140px, var(--paper) 820px, #ececec 870px);
  }
  .abs { position: absolute; }

  /* Header */
  .brand-name { left: 220px; top: 28px; font-size: 38px; font-weight: 400; color: var(--pink); letter-spacing: 1px; }
  .brand-tagline { left: 217px; top: 76px; font-size: 12.5px; color: #222; }
  .main-nav { left: 0; top: 44px; width: 1200px; height: 20px; }
  .main-nav a { position: absolute; font-size: 13.5px; color: #555; text-decoration: none; letter-spacing: .2px; }
  .nav-ring { left: 524px; top: 30px; }
  .new-tag { left: 755px; top: 10px; width: 58px; height: 30px; border-radius: 4px;
    background: linear-gradient(90deg, rgba(224,51,106,.25), rgba(80,80,80,.15)); }
  .double-rule { left: 212px; width: 767px; height: 7px; border-top: 2px solid var(--rule); border-bottom: 1px solid var(--rule); }

  /* Hero */
  .hero-title { left: 212px; top: 148px; font-size: 34px; line-height: 43px; font-weight: 700; color: var(--ink); letter-spacing: -.2px; }
  .hero-lead { left: 212px; top: 238px; width: 452px; font-size: 15px; line-height: 18.6px; color: #555; }
  .hero-note { left: 212px; top: 309px; width: 470px; font-size: 13px; line-height: 16px; color: #555; }
  .cta { top: 385px; width: 165px; height: 38px; border-radius: 3px; border: 1px solid var(--pink-dark);
    background: linear-gradient(180deg, #ee4b7f, var(--pink-dark)); color: #fff; font-size: 17px;
    display: flex; align-items: center; justify-content: center; text-decoration: none;
    box-shadow: inset 0 1px 0 rgba(255,255,255,.35), 0 1px 2px rgba(0,0,0,.2); }
  .slider-dots { left: 222px; top: 446px; display: flex; gap: 7px; }
  .slider-dots span { width: 11px; height: 11px; border-radius: 50%; background: var(--pink-soft); }
  .slider-dots span:first-child { background: #e55b88; }
  .hero-visual { left: 711px; top: 161px; width: 268px; height: 286px; border-radius: 6px;
    background: linear-gradient(180deg, #e0467a 0%, #d93a6c 55%, #cfcfcf 72%, rgba(255,255,255,0) 100%); }

  /* Features */
  .feature { top: 562px; }
  .feature-icon { height: 74px; border-radius: 6px; background: linear-gradient(180deg, #cfcfcf, #9a9a9a); }
  .feature-title { margin-top: 15px; font-size: 17.5px; line-height: 20.5px; font-weight: 700; color: var(--pink); letter-spacing: -.3px; white-space: nowrap; }
  .feature-body { margin-top: 14px; width: 205px; font-size: 10.5px; line-height: 12.4px; color: var(--muted); }
  .read-more { display: block; margin-top: 5px; font-size: 10.5px; color: var(--pink); text-decoration: none; }

  /* Footer */
  .site-footer { left: 0; top: 875px; width: 1200px; height: 287px; background: var(--footer); }
  .footer-edge { left: 0; top: 868px; }
  .footer-base { left: 0; top: 1113px; width: 1200px; height: 49px; background: var(--footer-deep); border-top: 1px dotted #444; }
  .footer-col h3 { font-size: 17.5px; font-weight: 700; color: var(--pink); margin-bottom: 12px; }
  .footer-col { top: 905px; }
  .footer-col ul { list-style: none; }
  .footer-col li { font-size: 12.5px; line-height: 18.8px; color: var(--footer-text); padding-left: 9px; position: relative; }
  .footer-col li::before { content: ""; position: absolute; left: 0; top: 7px; border-left: 3px solid var(--pink);
    border-top: 2.5px solid transparent; border-bottom: 2.5px solid transparent; }
  .email-field { left: 638px; top: 938px; width: 249px; height: 25px; background: #fff; border-radius: 3px;
    font-size: 13px; font-style: italic; color: #999; padding: 4px 12px; }
  .send-button { left: 893px; top: 937px; width: 83px; height: 27px; border-radius: 3px; border: 1px solid #8e1a3f;
    background: linear-gradient(180deg, #ee4b7f, var(--pink-dark)); color: #fff; font-size: 14px;
    display: flex; align-items: center; justify-content: center; }
  .footer-rule { left: 212px; top: 1054px; width: 767px; border-top: 1px dotted #666; }
  .follow-lettering { left: 223px; top: 1069px; width: 120px; height: 24px; border-radius: 3px;
    background: linear-gradient(90deg, #555, #3a3a3a); }
  .social-link { top: 1074px; font-size: 13px; font-weight: 600; color: #cfcfcf; display: flex; align-items: center; gap: 6px; }
  .social-link i { width: 12px; height: 12px; background: var(--pink); display: inline-block; border-radius: 2px; }
  .copyright { left: 235px; top: 1132px; font-size: 12px; color: #bbb; }
</style>
</head>
<body>

<header>
  <div class="abs brand-name">Vorlen</div>
  <div class="abs brand-tagline">The Customer Experience Framework</div>
  <svg class="abs nav-ring" width="70" height="48" viewBox="0 0 70 48" aria-hidden="true">
    <ellipse cx="35" cy="24" rx="32" ry="20" fill="none" stroke="#222" stroke-width="1.6" transform="rotate(-8 35 24)"/>
  </svg>
  <div class="abs new-tag" role="img" aria-label="Hand-written 'new' note with arrow pointing to Blog"></div>
  <nav class="abs main-nav">
    <a href="#" style="left:541px">HOME</a>
    <a href="#" style="left:609px">PRODUCTS</a>
    <a href="#" style="left:702px">SUPPORT</a>
    <a href="#" style="left:785px">BLOG</a>
    <a href="#" style="left:847px">ABOUT</a>
    <a href="#" style="left:917px">CONTACT</a>
  </nav>
  <div class="abs double-rule" style="top:99px"></div>
</header>

<section class="hero">
  <h1 class="abs hero-title">Create compelling<br>experiences for your customers.</h1>
  <p class="abs hero-lead">Vorlen is a customer experience application framework – it enables you to build highly differentiated business applications to deliver compelling experiences to your customers.</p>
  <p class="abs hero-note">Vorlen is designed for innovators who understand that unlocking opportunity in today’s competitive marketplace is driven by delivering a better customer experience.</p>
  <a class="abs cta" href="#" style="left:212px">Live Demo</a>
  <a class="abs cta" href="#" style="left:399px">Download</a>
  <div class="abs slider-dots"><span></span><span></span><span></span></div>
  <div class="abs hero-visual" role="img" aria-label="Illustration of a desktop monitor with pink swirl artwork and its reflection"></div>
  <div class="abs double-rule" style="top:473px"></div>
</section>

<section class="features">
  <article class="abs feature" style="left:236px">
    <div class="feature-icon" role="img" aria-label="Pencil sketch of a monitor" style="width:86px;margin-left:41px"></div>
    <h2 class="feature-title">Opportunity through<br>customer experience innovation</h2>
    <p class="feature-body" style="margin-top:12px">Turn the experience you deliver to your customers into competitive advantage. Vorlen’s customer experience framework is the flexible and practical way for enterprise organisations to create and manage compelling experiences. It gives you full control over how you wish to interact with your customers, and allows you to tailor experiences that grow your brand.</p>
    <a class="read-more" href="#">Read More...</a>
  </article>
  <article class="abs feature" style="left:518px">
    <div class="feature-icon" role="img" aria-label="Pencil sketch of three star-shaped snowflakes" style="width:156px"></div>
    <h2 class="feature-title">True differentiation</h2>
    <p class="feature-body" style="margin-top:14px">There is no one-size-fits-all application, because every business is unique! We believe in technology as a business differentiator, and flexible, cutting edge technology the key to success. If you’re serious about differentiation, and want to create powerful experiences to connect with your customers in exciting new ways, we can help create experiences that your competitors can’t match.</p>
    <a class="read-more" href="#">Read More...</a>
  </article>
  <article class="abs feature" style="left:772px">
    <div class="feature-icon" role="img" aria-label="Pencil sketch of a key" style="width:72px;margin-left:62px"></div>
    <h2 class="feature-title">Enterprise CX</h2>
    <p class="feature-body" style="margin-top:14px">Vorlen is committed to delivering enterprise solutions with the performance, scalability and security capabilities to support the largest and most complex organisations. SOA, application flexibility, cross-platform delivery, easy integration and efficient manageability which are built on standard web technologies. Plus its open-sourced under the OpenShare v3 licence which removes any fear of proprietary lock-in.</p>
    <a class="read-more" href="#">Read More...</a>
  </article>
</section>

<footer>
  <div class="abs site-footer"></div>
  <svg class="abs footer-edge" width="1200" height="8" viewBox="0 0 1200 8" preserveAspectRatio="none" aria-hidden="true">
    <defs>
      <pattern id="zigzag" width="10" height="8" patternUnits="userSpaceOnUse">
        <path d="M0 8 L0 7 L5 1 L10 7 L10 8 Z" fill="#1c1c1c"/>
      </pattern>
    </defs>
    <rect width="1200" height="8" fill="url(#zigzag)"/>
  </svg>

  <div class="abs footer-col" style="left:229px">
    <h3>Vorlen</h3>
    <ul><li>Home</li><li>Products</li><li>Support</li><li>Blog</li><li>About</li></ul>
  </div>
  <div class="abs footer-col" style="left:321px">
    <h3 style="margin-left:8px">Getting Started</h3>
    <ul><li>Demo</li><li>Documentation</li><li>Download</li></ul>
  </div>
  <div class="abs footer-col" style="left:495px">
    <h3 style="margin-left:8px">Support</h3>
    <ul><li>Contact Us</li><li>Vorlen Services</li><li>Vorlen Support</li></ul>
  </div>
  <div class="abs footer-col" style="left:638px">
    <h3>Join Our Mailing List</h3>
  </div>
  <div class="abs email-field">Email Address</div>
  <div class="abs send-button">Send</div>

  <div class="abs footer-rule"></div>
  <div class="abs follow-lettering" role="img" aria-label="Hand-lettered 'Follow us on:'"></div>
  <a class="abs social-link" style="left:354px"><i></i>Friendwall</a>
  <a class="abs social-link" style="left:442px">Linkfolio</a>

  <div class="abs footer-base"></div>
  <div class="abs copyright">© 2011 All Rights Reserved. Vorlen</div>
</footer>

</body>
</html>
```